Jade Pan Kitchen Chinese Takeaway Menu

We need the new menu design for our Jade Pan Kitchen chinese takeaway menu as all the resources are had been uploaded all of the photos must be in the menu,
Need a Dish Runner and Chatterly Logo on the Jade pan kitchen logo page
OPEN 7 DAYS Sun-Thu 10.00am - 9.00pm Fri-Sat 10.00am - 9.30pm
Shop 9, Marlowe Arcade 512 Keller St, Ashgrove QLD 4810
Phone: 07 4715 3362
The best fresh food around- no MSG used, and all dishes low in fat! YOU CAN ALSO MAKE YOUR OWN DISHES
Delivery in 3km radius, 5:00-9:00pm each day (charge applies). Prices effective June 2017. All prices inclusive of G.S.T. Prices subject to change.
Need space for another 9 Photos

I had been increase my Budget and want to get more designs to submit, the logo of DishRunner you can google it on the site, and i had been update the Brief, Please check it carefully, Thank you Added Thursday, June 22, 2017

Target Market(s)

Winner will invite to design the menu board

Industry/Entity Type

Inn

Font styles to use
Serif

Colors

Designer to choose colors to be used in the design.

Requirements
Must have
• Need a DishRunner and Chatterly Logo
• OPEN 7 DAYS Sun-Thu 10.00am - 9.00pm Fri-Sat 10.00am - 9.30pm
• Shop 9, Marlowe Arcade 512 Keller St, Ashgrove QLD 4810
• Phone: 07 4715 3362
• The best fresh food around- no MSG used, and all dishes low in fat! YOU CAN ALSO MAKE YOUR OWN DISHES
• Delivery in 3km radius, 5:00-9:00pm each day (charge applies). Prices effective June 2017. All prices inclusive of G.S.T. Prices subject to change.
• Need space for another 9 Photos
Nice to have
• Totally 58 Photos

```html
<!DOCTYPE html>
<html lang="en">
<head>
<meta charset="utf-8">
<title>Jade Pan Kitchen – Takeaway Menu</title>
<link href="https://fonts.googleapis.com/css2?family=Roboto+Condensed:ital,wght@0,400;0,700;1,700&family=Montserrat:wght@400;700&display=swap" rel="stylesheet">
<style>
  :root{
    --red:#e0222a;
    --red-dark:#b8141b;
    --ink:#1e1e1e;
    --paper:#efe9dc;
    --paper-edge:#ddd3bf;
    --charcoal:#3a3a3a;
    --charcoal-dark:#262626;
    --white:#ffffff;
    --muted:#8a8173;
  }
  *{box-sizing:border-box;margin:0;padding:0}
  html,body{width:1200px;height:1200px;overflow:hidden;background:#e6e4e1}
  body{font-family:"Roboto Condensed",Arial,sans-serif;color:var(--ink)}
  .menu{position:absolute;left:0;top:176px;width:1200px;height:848px;display:flex;box-shadow:0 10px 30px rgba(0,0,0,.25)}
  .panel{width:400px;height:848px;position:relative;overflow:hidden}
  .paper{background:radial-gradient(ellipse at 50% 40%,var(--paper) 55%,var(--paper-edge) 100%)}

  /* Dish list */
  .dish-list{list-style:none;padding:34px 26px 20px 20px;display:flex;flex-direction:column;gap:6px}
  .dish{display:grid;grid-template-columns:46px 1fr;gap:10px;align-items:center;height:47px}
  .dish-photo{width:44px;height:44px;border-radius:50%;border:3px solid var(--white);background:radial-gradient(circle,#d98b3a 0%,#b5532a 60%,#7a4a2a 100%);box-shadow:0 1px 3px rgba(0,0,0,.3)}
  .dish-head{display:flex;align-items:flex-end;gap:4px;border-bottom:1px dashed var(--red);padding-bottom:1px}
  .dish-name{color:var(--red);font-weight:700;font-style:italic;font-size:13px;white-space:nowrap}
  .dish-price{margin-left:auto;color:var(--red);font-weight:700;font-size:12px}
  .dish-desc{font-size:11px;line-height:1.2;margin-top:2px}

  /* Entrée */
  .entree-title{display:flex;align-items:center;gap:10px;padding:30px 24px 14px;font-weight:700;font-size:20px;letter-spacing:1px}
  .entree-title::before,.entree-title::after{content:"";flex:1;height:1px;background:var(--ink)}
  .entree-grid{display:grid;grid-template-columns:repeat(3,1fr);gap:10px 14px;padding:0 24px}
  .entree-item{text-align:center}
  .photo-slot{height:92px;background:var(--white);border-radius:10px;box-shadow:0 1px 4px rgba(0,0,0,.2);display:flex;align-items:center;justify-content:center;font-size:10px;color:var(--muted);line-height:1.2;text-transform:uppercase}
  .entree-name{color:var(--red);font-weight:700;font-size:11px;text-transform:uppercase;margin-top:6px}
  .entree-price{font-size:10px}

  .hours{margin:26px 24px 0;background:var(--red);color:var(--white);border-radius:6px;display:flex;align-items:center;padding:8px 12px;gap:12px}
  .hours-seven{font-size:54px;font-weight:700;line-height:1}
  .hours-open{font-size:20px;font-weight:700;line-height:1;text-transform:uppercase;border-right:1px solid var(--white);padding-right:12px}
  .hours-times{font-size:17px;line-height:1.3}
  .delivery{padding:16px 24px 0;color:var(--red)}
  .delivery-title{font-size:24px;font-weight:700;text-transform:uppercase}
  .delivery-time{font-size:16px;color:var(--ink)}
  .prices-title{font-size:20px;font-weight:700;color:var(--red);text-transform:uppercase;margin-top:6px}
  .prices-note{font-size:12px;color:var(--ink)}
  .contact{list-style:none;padding:18px 24px 0;display:flex;flex-direction:column;gap:8px;font-size:13px}
  .contact li{display:flex;align-items:center;gap:8px}
  .contact svg{flex:none}

  /* Cover */
  .cover{background:linear-gradient(160deg,var(--charcoal) 0%,var(--charcoal-dark) 100%)}
  .cover-art{position:absolute;inset:0}
  .brand{position:absolute;left:40px;top:60px;display:flex;align-items:center;gap:12px}
  .brand-mark{width:34px;height:34px;border-radius:50%;background:var(--red)}
  .brand-name{font-family:"Montserrat",Arial,sans-serif;font-weight:700;font-size:32px;color:var(--red)}
  .tagline{position:absolute;left:30px;right:30px;top:640px;text-align:center}
  .tagline-main{font-family:"Montserrat",Arial,sans-serif;font-weight:700;font-size:30px;color:var(--white)}
  .tagline-sub{font-family:"Montserrat",Arial,sans-serif;font-weight:700;font-size:20px;color:var(--red);text-transform:uppercase}
  .tagline-band{margin:10px -30px 0;background:var(--red);color:var(--white);font-weight:700;font-style:italic;font-size:22px;text-transform:uppercase;padding:6px 0}
  .tagline-extra{font-family:"Montserrat",Arial,sans-serif;font-size:13px;color:var(--white);text-transform:uppercase;margin-top:10px}
</style>
</head>
<body>
<main class="menu">

  <section class="panel paper" aria-label="Noodles and soups">
    <ul class="dish-list">
      <li class="dish"><div class="dish-photo" role="img" aria-label="Vegetarian goreng dish photo"></div><div><div class="dish-head"><span class="dish-name">44.Vegetarian Goreng</span><span class="dish-price">$11.50</span></div><p class="dish-desc">Thick Egg Noodles with Tofu &amp; Seasonal Vegetables in a light Curry Sauce</p></div></li>
      <li class="dish"><div class="dish-photo" role="img" aria-label="Garlic chilli beef dish photo"></div><div><div class="dish-head"><span class="dish-name">45.Garlic Chilli Beef</span><span class="dish-price">$11.90</span></div><p class="dish-desc">Thick Egg Noodles with Beef &amp; Seasonal Vegetables in a Garlic Chilli Sauce</p></div></li>
      <li class="dish"><div class="dish-photo" role="img" aria-label="Teriyaki chicken noodle dish photo"></div><div><div class="dish-head"><span class="dish-name">46.Teriyaki Chicken Noodle</span><span class="dish-price">$11.90</span></div><p class="dish-desc">Japanese Udon Noodles with Chicken &amp; Seasonal Vegetables in Teriyaki Sauce</p></div></li>
      <li class="dish"><div class="dish-photo" role="img" aria-label="Fried kwei teow dish photo"></div><div><div class="dish-head"><span class="dish-name">47.Fried Kwei Teow</span><span class="dish-price">$11.90</span></div><p class="dish-desc">Flat Rice Noodles with Roast Pork, Shrimp &amp; Seasonal Vegetables in a dark Soy Chilli Sauce</p></div></li>
      <li class="dish"><div class="dish-photo" role="img" aria-label="Black pepper beef dish photo"></div><div><div class="dish-head"><span class="dish-name">48.Black Pepper Beef</span><span class="dish-price">$11.90</span></div><p class="dish-desc">Japanese Udon Noodles with Beef &amp; Seasonal Vegetables in a Black Pepper Sauce</p></div></li>
      <li class="dish"><div class="dish-photo" role="img" aria-label="Combo chow mein dish photo"></div><div><div class="dish-head"><span class="dish-name">49.Combo Chow Mein</span><span class="dish-price">$14.90</span></div><p class="dish-desc">Crispy Fried Noodles with King Prawns, delicious Combo Meat &amp; Seasonal Vegetables in an Oyster Sauce</p></div></li>
      <li class="dish"><div class="dish-photo" role="img" aria-label="Pad thai dish photo"></div><div><div class="dish-head"><span class="dish-name">50.Pad Thai</span><span class="dish-price">$12.50</span></div><p class="dish-desc">Thai Flat Noodles with Chicken &amp; Seasonal Vegetables in Pad Thai Sauce</p></div></li>
      <li class="dish"><div class="dish-photo" role="img" aria-label="Carbonara dish photo"></div><div><div class="dish-head"><span class="dish-name">51.Carbonara</span><span class="dish-price">$11.90</span></div><p class="dish-desc">Fettuccine with Bacon, Onion &amp; Mushroom in a Rich Creamy Sauce</p></div></li>
      <li class="dish"><div class="dish-photo" role="img" aria-label="Beef noodle soup photo"></div><div><div class="dish-head"><span class="dish-name">52.Beef Noodle Soup</span><span class="dish-price">$11.90</span></div><p class="dish-desc">Thick Egg Noodles with Braised Beef &amp; Seasonal Vegetables in a hot hearty soup</p></div></li>
      <li class="dish"><div class="dish-photo" role="img" aria-label="Curry chicken laksa photo"></div><div><div class="dish-head"><span class="dish-name">53.Curry Chicken Laksa</span><span class="dish-price">$11.90</span></div><p class="dish-desc">Thick Egg Noodles with Chicken, Fish Cake, Tofu &amp; Seasonal Vegetables in a creamy Coconut Curry Soup</p></div></li>
      <li class="dish"><div class="dish-photo" role="img" aria-label="Seafood laksa photo"></div><div><div class="dish-head"><span class="dish-name">54.Seafood Laksa</span><span class="dish-price">$14.90</span></div><p class="dish-desc">Thick Egg Noodles with mixed Seafood, Tofu &amp; Seasonal Vegetables in a creamy Coconut Curry Soup</p></div></li>
      <li class="dish"><div class="dish-photo" role="img" aria-label="Won ton soup photo"></div><div><div class="dish-head"><span class="dish-name">55.Won Ton Soup</span><span class="dish-price">$12.90</span></div><p class="dish-desc">Thin Rice Noodles with home made Won Ton &amp; Seasonal Vegetables in a hot hearty soup</p></div></li>
      <li class="dish"><div class="dish-photo" role="img" aria-label="Tom yum soup photo"></div><div><div class="dish-head"><span class="dish-name">56.Tom Yum Soup</span><span class="dish-price">$13.90</span></div><p class="dish-desc">Thin Rice Noodles with Mixed Seafood &amp; Seasonal Vegetables in a Thai Hot &amp; Sour Soup</p></div></li>
      <li class="dish"><div class="dish-photo" role="img" aria-label="House combo soup photo"></div><div><div class="dish-head"><span class="dish-name">57.Jade-House Combo Soup</span><span class="dish-price">$13.90</span></div><p class="dish-desc">Thin Egg Noodles with Prawns, delicious Combo Meat &amp; Seasonal Vegetables in Chicken Soup</p></div></li>
      <li class="dish"><div class="dish-photo" role="img" aria-label="Beef or chicken udon soup photo"></div><div><div class="dish-head"><span class="dish-name">58.Beef / Chicken Udon Soup</span><span class="dish-price">$11.90</span></div><p class="dish-desc">Beef or Chicken &amp; Seasonal Vegetables in a Miso Soup</p></div></li>
    </ul>
  </section>

  <section class="panel paper" aria-label="Entrée and information">
    <h2 class="entree-title">ENTRÉE</h2>
    <div class="entree-grid">
      <div class="entree-item"><div class="photo-slot">Space<br>for<br>photos</div><p class="entree-name">Spring Rolls</p><p class="entree-price">$1.50EA / $5.00 4PK</p></div>
      <div class="entree-item"><div class="photo-slot">Space<br>for<br>photos</div><p class="entree-name">Dim Sims</p><p class="entree-price">$2.00EA / $6.00 4PK</p></div>
      <div class="entree-item"><div class="photo-slot">Space<br>for<br>photos</div><p class="entree-name">Tempura Prawns</p><p class="entree-price">$2.20EA / $8.00 4PK</p></div>
      <div class="entree-item"><div class="photo-slot">Space<br>for<br>photos</div><p class="entree-name">Prawn Chips</p><p class="entree-price">$2.50 BAG</p></div>
      <div class="entree-item"><div class="photo-slot">Space<br>for<br>photos</div><p class="entree-name">Crispy Noodles</p><p class="entree-price">$2.00</p></div>
      <div class="entree-item"><div class="photo-slot">Space<br>for<br>photos</div><p class="entree-name">Miso Soup</p><p class="entree-price">$3.00</p></div>
      <div class="entree-item"><div class="photo-slot">Space<br>for<br>photos</div><p class="entree-name">Chicken Corn Soup</p><p class="entree-price">$5.00</p></div>
      <div class="entree-item"><div class="photo-slot">Space<br>for<br>photos</div><p class="entree-name">Crispy Noodles</p><p class="entree-price">$2.00</p></div>
      <div class="entree-item"><div class="photo-slot">Space<br>for<br>photos</div><p class="entree-name">Miso Soup</p><p class="entree-price">$3.00</p></div>
    </div>

    <div class="hours">
      <span class="hours-seven">7</span>
      <span class="hours-open">Open<br>Days</span>
      <p class="hours-times">Sun-Thu : 10.00am - 9.00pm<br>Fri-Sat : 10.00am - 9.30pm</p>
    </div>

    <div class="delivery">
      <p class="delivery-title">Delivery in 3km radius</p>
      <p class="delivery-time">5:00-9:00pm each day (charge applies)</p>
      <p class="prices-title">Prices effective June 2017</p>
      <p class="prices-note">All prices inclusive of G.S.T. Prices subject to change.</p>
    </div>

    <ul class="contact">
      <li><svg width="16" height="16" viewBox="0 0 24 24"><path fill="#e0222a" d="M6.6 10.8a15 15 0 0 0 6.6 6.6l2.2-2.2a1 1 0 0 1 1-.25 11.4 11.4 0 0 0 3.6.57 1 1 0 0 1 1 1V20a1 1 0 0 1-1 1A17 17 0 0 1 3 4a1 1 0 0 1 1-1h3.5a1 1 0 0 1 1 1c0 1.25.2 2.45.57 3.6a1 1 0 0 1-.25 1z"/></svg>07 4715 3362</li>
      <li><svg width="16" height="16" viewBox="0 0 16 16"><rect width="16" height="16" rx="3" fill="#e0222a"/></svg>www.chatterly.com/pages/Jade-Pan-Kitchen/1048263</li>
      <li><svg width="16" height="16" viewBox="0 0 24 24"><path fill="#e0222a" d="M12 2a7 7 0 0 0-7 7c0 5.2 7 13 7 13s7-7.8 7-13a7 7 0 0 0-7-7zm0 9.5A2.5 2.5 0 1 1 12 6.5a2.5 2.5 0 0 1 0 5z"/></svg>Shop 9, Marlowe Arcade 512 Keller St, Ashgrove QLD 4810</li>
    </ul>
  </section>

  <section class="panel cover" aria-label="Front cover">
    <svg class="cover-art" width="400" height="848" viewBox="0 0 400 848">
      <defs>
        <linearGradient id="hero" x1="0" y1="0" x2="1" y2="1">
          <stop offset="0" stop-color="#e9c9a0"/>
          <stop offset=".5" stop-color="#e58b5c"/>
          <stop offset="1" stop-color="#7fa84a"/>
        </linearGradient>
        <radialGradient id="bowl1"><stop offset="0" stop-color="#c9a26a"/><stop offset=".75" stop-color="#7a3b1f"/><stop offset="1" stop-color="#4a2414"/></radialGradient>
        <radialGradient id="bowl2"><stop offset="0" stop-color="#e6a070"/><stop offset=".75" stop-color="#c86a3c"/><stop offset="1" stop-color="#1c1c1c"/></radialGradient>
      </defs>
      <path d="M0 170 C140 150 280 130 400 110 L400 560 C300 580 180 600 0 620 Z" fill="#ffffff"/>
      <path d="M0 160 C140 140 280 120 400 98 L400 110 C280 130 140 150 0 170 Z" fill="#e0222a"/>
      <path d="M0 620 C180 600 300 580 400 560 L400 574 C300 594 180 614 0 634 Z" fill="#e0222a"/>
      <path d="M70 190 C180 172 290 155 400 138 L400 530 C300 548 200 565 70 580 Z" fill="url(#hero)" role="img" aria-label="Noodle stir-fry with prawns and vegetables"/>
      <circle cx="240" cy="500" r="78" fill="url(#bowl2)" role="img" aria-label="Bowl of fried rice"/>
      <circle cx="330" cy="410" r="64" fill="url(#bowl1)" role="img" aria-label="Bowl of stir-fried beef and mushrooms"/>
    </svg>

    <div class="brand">
      <span class="brand-mark"></span>
      <span class="brand-name">Jade Pan Kitchen</span>
    </div>

    <div class="tagline">
      <p class="tagline-main">The best fresh food</p>
      <p class="tagline-sub">Around- no MSG used</p>
      <p class="tagline-band">All dishes low in fat!</p>
      <p class="tagline-extra">You can also make your own dishes</p>
    </div>
  </section>

</main>
</body>
</html>
```